Bref créative
Business Card, MS Letterhead Template, Envelopes, & E-mail Signature Template for Investment Firm
None - our logo already has the company name included in it
Simple
Peter Dawes
Managing Partner
436 West Fenwick Ave., Suite 210
Charlotte, NC 28202-2731
PDawes@BrambleRidgeLLP.example
www.BrambleRidgeWealthAdvisoryGroup.example
Looking for:
1) Business Cards
2) MS Word Letterhead Template
3) Envelopes - standard size
4) E-mail Signature Template for Outlook
Thanks in advance for your designs and time!
Uploaded the only AI file I have. It has four separate color variations of our logo. We want to use the main logo, which is the blue and gray one. We do not want to use the black and white ones.
This is our logo AI file. Please use the blue and gray one and not the black and white ones.

```html
<!DOCTYPE html>
<html lang="en">
<head>
<meta charset="utf-8">
<title>Bramble Ridge Wealth Advisory Group — Business Card</title>
<link href="https://fonts.googleapis.com/css2?family=Cinzel:wght@400;500&display=swap" rel="stylesheet">
<style>
  :root {
    --backdrop: #e6e3de;
    --card-white: #ffffff;
    --brand-blue: #263a86;
    --brand-grey: #8b8f98;
    --text-white: #ffffff;
    --tab-grey: #b9bcc2;
  }
  html, body {
    margin: 0;
    padding: 0;
    width: 1200px;
    height: 900px;
    overflow: hidden;
    background: var(--backdrop);
  }
  .canvas {
    position: relative;
    width: 1200px;
    height: 900px;
  }
  .business-card {
    position: absolute;
    left: 100px;
    top: 164px;
    width: 1000px;
    height: 572px;
    background: var(--card-white);
    box-shadow: 0 6px 24px rgba(0,0,0,0.18);
    overflow: hidden;
    font-family: "Cinzel", "Trajan Pro", serif;
  }
  .brand-lockup {
    position: absolute;
    left: 240px;
    top: 78px;
    display: flex;
    align-items: center;
    gap: 22px;
  }
  .brand-square {
    width: 70px;
    height: 70px;
    background: var(--brand-grey);
  }
  .brand-name {
    color: var(--brand-blue);
    font-weight: 400;
    line-height: 1;
  }
  .brand-name .primary {
    display: block;
    font-size: 44px;
    letter-spacing: 1px;
  }
  .brand-name .secondary {
    display: block;
    font-size: 17px;
    letter-spacing: 3.2px;
    margin-top: 8px;
  }
  .info-band {
    position: absolute;
    left: 0;
    top: 240px;
    width: 100%;
    height: 290px;
    background: var(--brand-blue);
  }
  .edge-tab {
    position: absolute;
    left: 0;
    top: 390px;
    width: 14px;
    height: 50px;
    background: var(--tab-grey);
    border-radius: 0 4px 4px 0;
  }
  .person {
    position: absolute;
    left: 42px;
    top: 392px;
    color: var(--text-white);
    font-size: 18px;
    line-height: 1.35;
    letter-spacing: 0.5px;
    text-transform: uppercase;
  }
  .contact-list {
    position: absolute;
    left: 520px;
    top: 256px;
    width: 450px;
    margin: 0;
    padding: 0;
    list-style: none;
    color: var(--text-white);
    font-size: 17px;
    text-transform: uppercase;
    letter-spacing: 0.3px;
  }
  .contact-list li {
    display: flex;
    align-items: flex-start;
    gap: 12px;
    margin-bottom: 9px;
    line-height: 1.3;
    white-space: nowrap;
  }
  .contact-list .icon {
    flex: none;
    width: 22px;
    height: 22px;
    margin-top: 1px;
  }
  .contact-list .small {
    font-size: 13px;
    letter-spacing: 0;
    line-height: 24px;
  }
</style>
</head>
<body>
<div class="canvas">
  <div class="business-card">
    <div class="brand-lockup">
      <div class="brand-square"></div>
      <div class="brand-name">
        <span class="primary">Bramble Ridge</span>
        <span class="secondary">Wealth Advisory Group</span>
      </div>
    </div>

    <div class="info-band"></div>
    <div class="edge-tab"></div>

    <div class="person">
      <div class="person-name">Peter Dawes</div>
      <div class="person-title">Managing Partner</div>
    </div>

    <ul class="contact-list">
      <li>
        <svg class="icon" viewBox="0 0 22 22"><circle cx="11" cy="11" r="11" fill="#fff"/><path d="M11 5a4 4 0 0 1 4 4c0 3-4 8-4 8s-4-5-4-8a4 4 0 0 1 4-4z" fill="#263a86"/><circle cx="11" cy="9" r="1.5" fill="#fff"/></svg>
        <span>436 West Fenwick Ave., Suite 210<br>Charlotte, NC 28202-2731</span>
      </li>
      <li>
        <svg class="icon" viewBox="0 0 22 22"><circle cx="11" cy="11" r="11" fill="#fff"/><path d="M7 6l2.5-.5 1.2 3-1.5 1a7 7 0 0 0 3.3 3.3l1-1.5 3 1.2L16 15c-5 .5-9.5-4-9-9z" fill="#263a86"/></svg>
        <span>704-555-0140</span>
      </li>
      <li>
        <svg class="icon" viewBox="0 0 22 22"><circle cx="11" cy="11" r="11" fill="#fff"/><rect x="7.5" y="4.5" width="7" height="13" rx="1.2" fill="#263a86"/><rect x="8.7" y="6" width="4.6" height="8" fill="#fff"/></svg>
        <span>704-555-0182</span>
      </li>
      <li>
        <svg class="icon" viewBox="0 0 22 22"><circle cx="11" cy="11" r="11" fill="#fff"/><rect x="5.5" y="9" width="11" height="7" rx="1" fill="#263a86"/><rect x="8" y="5" width="6" height="5" fill="#263a86"/><rect x="8" y="12" width="6" height="1.2" fill="#fff"/></svg>
        <span>704-555-0141</span>
      </li>
      <li>
        <svg class="icon" viewBox="0 0 22 22"><circle cx="11" cy="11" r="11" fill="#fff"/><rect x="5" y="7" width="12" height="8.5" rx="1" fill="#263a86"/><path d="M5.5 7.5L11 12l5.5-4.5" fill="none" stroke="#fff" stroke-width="1.2"/></svg>
        <span class="small">PDawes@BrambleRidgeLLP.example</span>
      </li>
      <li>
        <svg class="icon" viewBox="0 0 22 22"><circle cx="11" cy="11" r="11" fill="#fff"/><circle cx="11" cy="11" r="6" fill="none" stroke="#263a86" stroke-width="1.4"/><ellipse cx="11" cy="11" rx="2.6" ry="6" fill="none" stroke="#263a86" stroke-width="1.2"/><line x1="5" y1="11" x2="17" y2="11" stroke="#263a86" stroke-width="1.2"/></svg>
        <span class="small">www.BrambleRidgeWealthAdvisoryGroup.example</span>
      </li>
    </ul>
  </div>
</div>
</body>
</html>
```